Create a Graphic About YOURSELF and PixelHarbor

PixelHarbor would like you (designers) to create an awesome graphic to promote YOURSELF and your profile on PixelHarbor!

Your graphic should communicate your name, your services and should mention PixelHarbor.

The design should be perfect for sharing on Chatterly. Here's an example of what we'd like http://blog.pixelharbor-example.ca/article/333/pixelharbor-launches-3000-hire-me-social-design-contest

Once you submitted your design, we'd love you to share the design ('advertisement') and promote yourself and PixelHarbor to your friends and potential customers. So make your submissions great and get your friends to vote for your design by 'Liking' it on Chatterly!

Prizes:
$1500 - "PixelHarbor Community" prize awarded to the designer with the most Chatterly 'Likes'
5 x $50 for the next 5 'most liked' designs on Chatterly

$1000 - "Hire Me" prize awarded to the designer who receives the most client invites
5 x $50 for the next 5 'most invited' designers

In summary, this is a great opportunity for you to increase your exposure to PixelHarbor customers and win cash prizes. Show off your design skills and get hired by PixelHarbor customers from around the world!

Target Market(s)

Fans, friends and customers of YOU

Industry/Entity Type

Cash

Requirements
Must have
• 1) Include your PixelHarbor user name on the graphic so customers can find you in the PixelHarbor Designer Directory
2) Include the tagline "Hire Me on PixelHarbor.com!" in your graphic design.
3) Share your design's URL on our Chatterly wall at http://chatterly-example.com/pixelharbor and get your friends to 'like' your design.
Nice to have
• 1) Include a tagline that expresses your design approach/philosophy
2) Artwork dimensions: 403 x 403 px
3) You can submit more than 1 design!
Should not have
• You must own the copyright of any images you use including stock imagery.

```html
<!DOCTYPE html>
<html lang="en">
<head>
<meta charset="utf-8">
<title>Hire Me on PixelHarbor</title>
<link rel="stylesheet" href="https://fonts.googleapis.com/css2?family=Cabin+Sketch:wght@700&family=Rubik+Dirt&family=Indie+Flower&family=PT+Sans&family=PT+Serif&display=swap">
<style>
  :root {
    --backdrop: #f4d78f;
    --parchment-light: #e9cf86;
    --parchment-mid: #d8b666;
    --parchment-edge: #a9793a;
    --services-blue: #1f6f9c;
    --headline-grey: #4f4f4f;
    --frame-grey: #5b5b5b;
    --bubble-fill: #fbe4cb;
    --bubble-ink: #d6168f;
    --ink: #111111;
    --brand-dark: #2b2b2b;
    --brand-blue: #1a78a8;
  }
  html, body {
    margin: 0;
    padding: 0;
    overflow: hidden;
  }
  .poster {
    position: relative;
    width: 1200px;
    height: 1200px;
    background: var(--backdrop);
    overflow: hidden;
  }
  .poster__shapes {
    position: absolute;
    inset: 0;
  }
  .services {
    position: absolute;
    left: 52px;
    top: 58px;
    margin: 0;
    font-family: "Cabin Sketch", cursive;
    font-weight: 700;
    font-size: 104px;
    line-height: 158px;
    color: var(--services-blue);
    letter-spacing: -1px;
  }
  .services span { display: block; }
  .thought {
    position: absolute;
    left: 812px;
    top: 102px;
    width: 260px;
    margin: 0;
    font-family: "Indie Flower", cursive;
    font-size: 34px;
    line-height: 40px;
    color: var(--bubble-ink);
    text-align: center;
    transform: rotate(8deg);
  }
  .headline {
    position: absolute;
    left: 0;
    width: 1210px;
    top: 560px;
    margin: 0;
    text-align: center;
    font-family: "Rubik Dirt", system-ui, sans-serif;
    font-size: 218px;
    line-height: 1;
    color: var(--headline-grey);
    letter-spacing: 4px;
  }
  .platform {
    position: absolute;
    left: 245px;
    top: 888px;
    display: flex;
    align-items: center;
    gap: 18px;
  }
  .platform__on {
    font-family: "PT Serif", serif;
    font-size: 58px;
    color: var(--brand-dark);
  }
  .platform__dot {
    width: 66px;
    height: 66px;
    border-radius: 50%;
    background: var(--brand-blue);
  }
  .platform__name {
    font-family: "PT Sans", sans-serif;
    font-size: 78px;
    color: var(--brand-dark);
  }
</style>
</head>
<body>
<main class="poster">
  <svg class="poster__shapes" width="1200" height="1200" viewBox="0 0 1200 1200">
    <defs>
      <radialGradient id="parchment-tone" cx="50%" cy="45%" r="70%">
        <stop offset="0%" stop-color="var(--parchment-light)"/>
        <stop offset="75%" stop-color="var(--parchment-mid)"/>
        <stop offset="100%" stop-color="var(--parchment-edge)"/>
      </radialGradient>
      <linearGradient id="portrait-tone" x1="0" y1="0" x2="0" y2="1">
        <stop offset="0%" stop-color="#a9a257"/>
        <stop offset="55%" stop-color="#c9b173"/>
        <stop offset="100%" stop-color="#e2cf93"/>
      </linearGradient>
    </defs>
    <rect class="parchment" x="12" y="14" width="1172" height="1182" rx="30"
          fill="url(#parchment-tone)" role="img" aria-label="Aged, burnt-edged parchment sheet"/>
    <ellipse class="portrait" cx="598" cy="652" rx="283" ry="348"
             fill="url(#portrait-tone)" role="img" aria-label="Stylised portrait of the designer"/>
    <ellipse class="portrait-frame" cx="598" cy="652" rx="290" ry="355"
             fill="none" stroke="var(--frame-grey)" stroke-width="14"/>
    <g class="thought-bubble" fill="var(--bubble-fill)" stroke="var(--ink)" stroke-width="4">
      <circle cx="940" cy="186" r="150"/>
      <circle cx="990" cy="378" r="22"/>
      <circle cx="965" cy="432" r="15"/>
      <circle cx="922" cy="455" r="10"/>
    </g>
  </svg>

  <h2 class="services">
    <span>Logo.</span>
    <span>Brochure.</span>
    <span>Graphic</span>
  </h2>

  <p class="thought">let me do the design! just IMAGINE!</p>

  <h1 class="headline">HIRE ME</h1>

  <p class="platform">
    <span class="platform__on">on</span>
    <span class="platform__dot"></span>
    <span class="platform__name">PixelHarbor</span>
  </p>
</main>
</body>
</html>
```